Web design for a honey company

We are a honey retailing company currently looking for creative design for 3 pages of our existing e-commerce website which can be found here www.stage.tovelprovisions.co.nz. The designs need to be responsive i.e. presented in both desktop and mobile versions. We want to use the existing page color pallet, however any fonts can be used. Please use the texts and graphic content in the attachment files provided. For more detailed instructions please. The page does not require coding, the output files should be provided as layered and editable PSD.<br/><br/>Task 2: design 2 home page banners. Images, texts and the concept provided in the "layout structure" file. <br/><br/>The web designs should be presented in both desktop and mobile versions. We are looking for professional designer submissions only!

Target Market(s)

Hi-end consumers
Health conscious consumers

Number of Pages Required

3 page

Requirements
Must have
• 50% of images supplied along + any suggested stock images.
• Supplied texts integrated in the designs.
• Please only use the product images we have provided!
Should not have
• Clipart vector bees, vector honey slots or combs.
• No images of honey in glass jars!
• Do not use images of the traditional honey wooden spoons!
• Do not use images of any other but Manuka flower!

```html
<!DOCTYPE html>
<html lang="en">
<head>
<meta charset="utf-8">
<title>Tovel — Manuka Honey</title>
<link href="https://fonts.googleapis.com/css2?family=Lexend:wght@500;600;700&family=Poppins:wght@400;500&family=Alfa+Slab+One&family=Oswald:wght@500&family=Varela+Round&display=swap" rel="stylesheet">
<style>
:root{
  --cream:#fcf5e3;
  --honey:#e2b43a;
  --honey-deep:#d19a1a;
  --gold:#d8a63c;
  --pale:#f7e6b0;
  --ink:#1f1f1f;
  --text:#3a3a3a;
  --jar:#2a1a14;
}
*{margin:0;padding:0;box-sizing:border-box}
html,body{width:1200px;height:3250px;overflow:hidden}
body{background:var(--cream);font-family:'Poppins',sans-serif;color:var(--text);position:relative}
.abs{position:absolute}
.hero-blob{position:absolute;left:0;top:0}
.brand{position:absolute;font-family:'Lexend',sans-serif;font-weight:700;color:var(--ink);letter-spacing:3px}
.brand-top{left:86px;top:44px;font-size:34px}
.nav{position:absolute;top:62px;left:0;width:1200px;font-size:14px;text-transform:uppercase;letter-spacing:.4px}
.nav a{position:absolute;color:#4a4030;text-decoration:none}
.nav a.active{font-weight:500;color:var(--ink)}
.btn-dark{position:absolute;background:var(--ink);color:#fff;font-family:'Lexend',sans-serif;font-weight:500;display:flex;align-items:center;justify-content:center;border-radius:3px}
.btn-gold{position:absolute;background:var(--gold);color:#fff;font-family:'Lexend',sans-serif;font-weight:500;display:flex;align-items:center;justify-content:center;border-radius:3px;font-size:16px;text-transform:uppercase}
.hero-title{position:absolute;left:0;width:1200px;top:155px;text-align:center;font-family:'Alfa Slab One',serif;font-size:58px;line-height:62px;color:#fff6dc;-webkit-text-stroke:2px #b8860b;letter-spacing:1px}
.art{position:absolute;border-radius:14px}
.arrow{position:absolute;width:52px;height:52px;border-radius:50%;display:flex;align-items:center;justify-content:center}
.section-title{position:absolute;left:0;width:1200px;text-align:center;font-family:'Lexend',sans-serif;font-weight:700;font-size:37px;color:var(--ink);letter-spacing:-.5px}
.product{position:absolute;width:220px;text-align:center;top:852px}
.product .halo{position:absolute;left:100px;top:25px;width:110px;height:140px;border-radius:0 80px 80px 0;background:#f8e7b7}
.product .jar{position:absolute;left:56px;top:0;width:107px;height:189px;border-radius:12px;background:linear-gradient(180deg,#1a1a1a 0 20%,var(--jar) 20% 100%)}
.product .name{position:absolute;top:218px;width:220px;font-family:'Varela Round',sans-serif;font-size:22px;color:var(--gold)}
.product .price{position:absolute;top:250px;width:220px;font-family:'Oswald',sans-serif;font-size:34px;color:var(--ink)}
.news-title{position:absolute;left:650px;width:430px;top:1413px;text-align:center;font-family:'Lexend',sans-serif;font-weight:700;font-size:38px;line-height:42px;color:var(--ink)}
.news-copy{position:absolute;left:672px;width:386px;top:1516px;text-align:center;font-size:15px;line-height:26px}
.field{position:absolute;left:679px;width:365px;height:62px;background:var(--pale);border-radius:3px;display:flex;align-items:center;padding-left:48px;font-size:15px;color:var(--gold)}
.field svg{position:absolute;left:14px}
.video{position:absolute;left:209px;top:2115px;width:782px;height:415px;background:#fff;padding:5px;box-shadow:0 0 6px rgba(0,0,0,.08)}
.video .frame{width:100%;height:100%;background:linear-gradient(90deg,#d9dbd8,#b9bcb7 55%,#8f928c)}
.play{position:absolute;left:551px;top:2272px;width:100px;height:100px;border-radius:50%;background:#fff;border:8px solid #e6c55e;display:flex;align-items:center;justify-content:center}
.about-copy{position:absolute;left:212px;width:776px;top:2568px;text-align:center;font-size:15px;line-height:27px}
.footer-wave{position:absolute;left:0;top:2800px}
.foot-head{position:absolute;font-family:'Lexend',sans-serif;font-weight:600;font-size:20px;color:var(--ink)}
.foot-list{position:absolute;list-style:none;font-size:15px;color:#3b3220}
.foot-list li{height:32px}
.social{position:absolute;top:3051px;width:42px;height:42px;background:#fff}
.contact-card{position:absolute;left:758px;top:2812px;width:365px;height:290px;background:#fff;border:6px solid #f1d980}
.contact-card h4{position:absolute;left:44px;top:46px;font-family:'Lexend',sans-serif;font-weight:600;font-size:20px;color:var(--ink)}
.contact-item{position:absolute;left:85px;font-size:14.5px;line-height:25px;color:#333}
.contact-item.muted{color:#888}
.contact-card svg{position:absolute;left:46px}
.rule{position:absolute;left:0;top:3167px;width:1200px;height:1px;background:rgba(255,255,255,.35)}
.copyright{position:absolute;left:0;width:1200px;top:3198px;text-align:center;font-size:14px;color:#f6e3a2}
</style>
</head>
<body>

<svg class="hero-blob" width="1200" height="600" viewBox="0 0 1200 600">
  <defs><linearGradient id="hg" x1="0" y1="0" x2="0" y2="1"><stop offset="0" stop-color="#f0cf5e"/><stop offset="1" stop-color="#d9a521"/></linearGradient></defs>
  <path d="M345 0 C330 60 300 95 220 110 C120 130 70 240 78 360 C86 470 200 580 330 585 L880 585 C980 570 1040 520 1100 500 C1150 470 1130 330 1110 250 C1080 140 1110 60 1080 0 Z" fill="url(#hg)"/>
</svg>

<div class="brand brand-top">TOVEL</div>

<nav class="nav">
  <a class="active" style="left:430px">Home</a>
  <a style="left:509px">MGO Manuka Honey</a>
  <a style="left:695px">About Us</a>
  <a style="left:800px">Contact Us</a>
</nav>
<div class="btn-dark" style="left:922px;top:42px;width:125px;height:51px;font-size:16px">BUY NOW</div>

<h1 class="hero-title">SOMETHING EXCITING<br>IS HAPPENING!</h1>

<div class="art" role="img" aria-label="Honey bee illustration" style="left:997px;top:183px;width:200px;height:215px;border-radius:50%;background:radial-gradient(circle,#8a5a1e,#c58a2c 55%,rgba(230,200,120,0))"></div>
<div class="art" role="img" aria-label="Honey bee illustration" style="left:50px;top:404px;width:152px;height:158px;border-radius:50%;background:radial-gradient(circle,#8a5a1e,#c58a2c 55%,rgba(230,200,120,0))"></div>
<div class="art" role="img" aria-label="Row of Manuka honey jars" style="left:343px;top:322px;width:515px;height:366px;background:linear-gradient(180deg,#1b1b1b 0 16%,#2d1b14 16% 100%)"></div>

<div class="arrow" style="left:231px;top:606px;border:2px solid var(--gold)">
  <svg width="20" height="14" viewBox="0 0 20 14"><path d="M19 7H2M7 1L1 7l6 6" fill="none" stroke="#d8a63c" stroke-width="2"/></svg>
</div>
<div class="arrow" style="left:919px;top:606px;background:#f4d86a">
  <svg width="20" height="14" viewBox="0 0 20 14"><path d="M1 7h17M13 1l6 6-6 6" fill="none" stroke="#b07d10" stroke-width="2"/></svg>
</div>

<h2 class="section-title" style="top:765px">OUR PRODUCTS</h2>

<div class="product" style="left:86px"><div class="halo"></div><div class="jar" role="img" aria-label="Manuka honey jar"></div><div class="name">Manuka Honey</div><div class="price">$ 15.00</div></div>
<div class="product" style="left:354px"><div class="halo"></div><div class="jar" role="img" aria-label="Manuka honey jar"></div><div class="name">Manuka Honey</div><div class="price">$ 15.00</div></div>
<div class="product" style="left:623px"><div class="halo"></div><div class="jar" role="img" aria-label="Manuka honey jar"></div><div class="name">Manuka Honey</div><div class="price">$ 15.00</div></div>
<div class="product" style="left:892px"><div class="halo"></div><div class="jar" role="img" aria-label="Manuka honey jar"></div><div class="name">Manuka Honey</div><div class="price">$ 15.00</div></div>

<div class="btn-gold" style="left:469px;top:1199px;width:260px;height:50px">Buy now our products</div>

<svg class="abs" style="left:0;top:1320px" width="1200" height="650" viewBox="0 0 1200 650">
  <path d="M540 450 C600 400 640 330 655 230 C670 110 750 15 870 12 C1010 10 1125 120 1123 300 C1120 470 990 630 840 628 C750 627 650 600 580 585" fill="none" stroke="#d8a63c" stroke-width="2"/>
</svg>
<div class="art" role="img" aria-label="Manuka honey jars with honeycomb and honey pool" style="left:76px;top:1432px;width:530px;height:518px;border-radius:20px 20px 200px 20px;background:linear-gradient(135deg,#2a1a14 0 45%,#e8a92a 70%,#f6cc4a)"></div>

<h2 class="news-title">SIGN UP TO<br>OUR NEWSLETTER</h2>
<p class="news-copy">Lorem ipsum dolor sit amet, consectetur adipiscing elit, sed do eiusmod tempor there incididunt ut labore et dolore magna aliqua.</p>
<div class="field" style="top:1630px"><svg width="20" height="20" viewBox="0 0 20 20"><circle cx="10" cy="6" r="5" fill="#d8a63c"/><path d="M1 20c0-6 4-8 9-8s9 2 9 8z" fill="#d8a63c"/></svg>Enter Name :</div>
<div class="field" style="top:1709px"><svg width="20" height="16" viewBox="0 0 20 16"><rect x="1" y="1" width="18" height="14" fill="none" stroke="#d8a63c" stroke-width="2"/><path d="M1 1l9 8 9-8" fill="none" stroke="#d8a63c" stroke-width="2"/></svg>Enter Email :</div>
<div class="btn-dark" style="left:679px;top:1813px;width:167px;height:51px;font-size:16px">SUBCRIBE NOW</div>

<h2 class="section-title" style="top:2025px">ABOUT COMPANY</h2>
<div class="video"><div class="frame" role="img" aria-label="Honey processing facility video still"></div></div>
<div class="play"><svg width="26" height="30" viewBox="0 0 26 30"><path d="M2 2l22 13L2 28z" fill="#d8a63c"/></svg></div>
<p class="about-copy">Lorem ipsum dolor sit amet, consectetur adipiscing elit, sed do eiusmod tempor incididunt ut labore et dolore magna aliqua. Ut enim ad minim veniam, quis nostrud exercitation ullamco laboris nisi ut aliquip deserunt mollit anim id est laborum.</p>
<div class="btn-gold" style="left:522px;top:2678px;width:156px;height:52px">Watch vedio</div>

<svg class="footer-wave" width="1200" height="450" viewBox="0 0 1200 450">
  <defs><linearGradient id="fg" x1="0" y1="0" x2="0" y2="1"><stop offset="0" stop-color="#f0cf5e"/><stop offset="1" stop-color="#d9a521"/></linearGradient></defs>
  <path d="M0 70 C120 10 300 0 450 40 C600 80 700 40 800 30 L1200 60 L1200 450 L0 450 Z" fill="url(#fg)"/>
</svg>

<div class="brand" style="left:96px;top:2950px;font-size:36px">TOVEL</div>
<div class="social" style="left:77px" aria-label="Social link"></div>
<div class="social" style="left:129px" aria-label="Social link"></div>
<div class="social" style="left:181px" aria-label="Social link"></div>

<div class="foot-head" style="left:337px;top:2915px">COMPANY</div>
<ul class="foot-list" style="left:337px;top:2966px"><li>Home</li><li>Mgo manuka honey</li><li>About</li><li>Company</li></ul>
<div class="foot-head" style="left:555px;top:2915px">LINKS</div>
<ul class="foot-list" style="left:555px;top:2966px"><li>Help</li><li>Testimonials</li><li>Terms &amp; conditions</li><li>Privacy Policy</li></ul>

<div class="contact-card">
  <h4>GET IN TOUCH</h4>
  <svg style="top:96px" width="16" height="22" viewBox="0 0 16 22"><path d="M8 0a8 8 0 0 0-8 8c0 6 8 14 8 14s8-8 8-14a8 8 0 0 0-8-8z" fill="#1f1f1f"/><circle cx="8" cy="8" r="3" fill="#fff"/></svg>
  <div class="contact-item muted" style="top:96px">123,Address, State Name, Street<br>Name, City Name, Zipcode</div>
  <svg style="top:164px" width="20" height="20" viewBox="0 0 20 20"><path d="M4 1l4 4-2 3c1 3 3 5 6 6l3-2 4 4-3 3C8 19 1 12 1 4z" fill="#1f1f1f"/></svg>
  <div class="contact-item" style="top:159px">+64 21 000 4417&nbsp; ( Whatsapp)</div>
  <svg style="top:216px" width="20" height="14" viewBox="0 0 20 14"><rect width="20" height="14" fill="#1f1f1f"/><path d="M1 1l9 7 9-7" fill="none" stroke="#fff" stroke-width="1.5"/></svg>
  <div class="contact-item" style="top:211px">sales@tovelprovisions.co.nz</div>
</div>

<div class="rule"></div>
<div class="copyright">Copyright © TOVEL - 2020 . All Right Reserved.</div>

</body>
</html>
```